Cybersecurity Start-Up - Tervalo

We need a power-point design for a new company based in Madrid (Spain) called 'Tervalo'. We aim to provide cybersecurity services to small- medium size companies for whom security is critical but paying big money to huge companies is not affordable.

The final design should communicate several things. As technology company which provides cybersecurity, it should be seen as something modern and futuristic , combined with safety and protection.

The company name Tervalo comes from Tervalosa, an ancient Celtiberian settlement in Spain which is famous for its role in the Celtiberian Wars (130 BC). They fought with Rome for 20 years , while being numerical inferior. And they won several times. When a final siege ocurred after a massive deployment of Rome legions, they held their ground for more than a year without food. When the situation was not longer sustainable, they decided to commit suicide rather than become slaves.

So the vision to hold the ground no matter what, should be communicated too
Updates

Need extra days to review

Requirements
Must have
• Check files attached for the logo of the company

```html
<!DOCTYPE html>
<html lang="en">
<head>
<meta charset="utf-8">
<title>Tervalo – Presentation Template</title>
<link href="https://fonts.googleapis.com/css2?family=Poppins:wght@400;600;700&family=Open+Sans:wght@400;600;700&display=swap" rel="stylesheet">
<style>
:root{
  --orange:#f15a24;
  --amber:#f7941d;
  --navy:#1b2535;
  --grey:#8b9099;
  --light:#eef0f3;
  --text:#3c4350;
  --bg1:#ececec;
  --bg2:#cfcfcf;
}
*{margin:0;padding:0;box-sizing:border-box}
html,body{width:857px;height:1200px;overflow:hidden}
body{background:radial-gradient(ellipse at 50% 40%,var(--bg1),var(--bg2));font-family:"Open Sans",sans-serif;color:var(--text);position:relative}
.slide{position:absolute;width:241px;height:180px;background:#fff;overflow:hidden;box-shadow:0 2px 5px rgba(0,0,0,.25)}
.abs{position:absolute}
.s-title{position:absolute;left:13px;top:13px;font:600 10.5px/1 "Poppins",sans-serif;color:var(--orange);letter-spacing:.2px}
.brand{position:absolute;right:11px;top:13px;font:600 8px/1 "Poppins",sans-serif;color:var(--navy)}
.foot{position:absolute;left:0;right:0;bottom:0;height:11px;background:var(--navy)}
.foot-url{position:absolute;left:14px;top:4px;font:600 2.8px/1 "Open Sans",sans-serif;color:#fff;letter-spacing:.2px}
.page{position:absolute;right:0;bottom:0;width:24px;height:15px;background:var(--orange);border-top-left-radius:12px;color:#fff;font:600 4.5px/1 "Poppins",sans-serif;text-align:center;padding-top:7px;padding-left:4px}
.tiny{font-size:3.4px;line-height:1.4}
.small{font-size:4.2px;line-height:1.45}
.bold{font-weight:700;color:var(--navy)}
.cover-brand{position:absolute;left:20px;top:30px;font:600 15px/1 "Poppins",sans-serif;color:var(--navy)}
.cover-title{position:absolute;left:0;right:0;top:80px;text-align:center;font:700 12.5px/1 "Poppins",sans-serif;color:#fff}
.cover-sub{position:absolute;left:0;right:0;top:95px;text-align:center;font:400 5.8px/1 "Open Sans",sans-serif;color:var(--navy)}
.icon-dot{position:absolute;width:18px;height:18px;border-radius:50%;display:flex;align-items:center;justify-content:center}
.row-text{position:absolute;left:67px;width:50px}
.row-head{font:700 3.6px/1.3 "Open Sans",sans-serif;color:var(--navy)}
.num{position:absolute;width:16px;height:16px;color:#fff;font:600 6px/16px "Poppins",sans-serif;text-align:center}
.grid-text{position:absolute;width:78px}
.grid-text h4{font:600 6px/1.1 "Poppins",sans-serif;color:var(--navy)}
.grid-text p{font-size:4px;line-height:1.3}
.right{text-align:right}
.pill-head{font:700 4.8px/1 "Poppins",sans-serif;color:var(--navy);padding-bottom:2px;border-bottom:.5px solid #c9ccd2;margin-bottom:2px;width:62px}
.checks li{list-style:none;font-size:4px;line-height:1;margin-bottom:4.4px;display:flex;align-items:center;gap:2px}
.photo{position:absolute}
.table{position:absolute;left:23px;top:57px;width:195px;border-collapse:collapse}
.table th{font:600 3.6px/9px "Open Sans",sans-serif;color:#fff;text-align:center;height:9px}
.table td{font-size:3.4px;height:10px;text-align:center;color:var(--text);border-right:.5px solid #fff}
.table tr:nth-child(odd) td{background:#f1f2f4}
.table tr:nth-child(even) td{background:#e4e7eb}
.table td:first-child{text-align:left;padding-left:5px}
.table tr:last-child td{border-bottom:1.5px solid #9aa6b8}
.center{text-align:center}
.pct{position:absolute;width:50px;text-align:center}
.person{position:absolute;width:70px;text-align:center}
.avatar{width:32px;height:32px;border-radius:50%;border:2px solid var(--orange);background:linear-gradient(160deg,#c9d3df,#7d8a9c);margin:0 auto 4px}
.person h5{font:600 5.6px/1 "Poppins",sans-serif;color:var(--navy);margin-bottom:3px}
.contact li{list-style:none;font-size:3.3px;line-height:1;margin-bottom:4px;display:flex;align-items:center;gap:3px}
.contact i{display:inline-block;width:4px;height:4px;border-radius:50%;border:.7px solid var(--orange)}
</style>
</head>
<body>

<!-- Row 1 -->
<section class="slide" style="left:51px;top:15px;background:linear-gradient(135deg,#f26a2b,#ee5522)">
  <div class="cover-brand">Tervalo</div>
  <h1 class="cover-title">PRESENTATION TITLE HERE</h1>
  <p class="cover-sub">Presentation Subtitle Goes Here</p>
</section>

<section class="slide" style="left:308px;top:15px;background:linear-gradient(135deg,#f8a025,#f4881a)">
  <div class="cover-brand">Tervalo</div>
  <h1 class="cover-title">PRESENTATION TITLE HERE</h1>
  <p class="cover-sub">Presentation Subtitle Goes Here</p>
</section>

<section class="slide" style="left:566px;top:15px">
  <div class="photo" role="img" aria-label="Photo of a security analyst at a computer, tinted orange" style="left:92px;top:0;width:149px;height:169px;background:linear-gradient(90deg,rgba(255,255,255,1) 0%,#f5b893 22%,#e9773f 60%,#c4582f 100%)"></div>
  <h2 class="s-title">TITLE GOES HERE</h2>
  <div class="brand">Tervalo</div>
  <div class="icon-dot" style="left:42px;top:50px;background:var(--navy)"><svg width="9" height="8" viewBox="0 0 9 8"><rect x=".5" y=".5" width="8" height="5" fill="none" stroke="#fff" stroke-width=".8"/><path d="M3 7.5h3M4.5 5.5v2" stroke="#fff" stroke-width=".8"/></svg></div>
  <div class="row-text" style="top:50px"><div class="row-head">TEXT GOES HERE</div><p class="tiny">Lorem ipsum dolor sit amet, tempor incididunt ut labore et dolore magna aliqua.</p></div>
  <div class="icon-dot" style="left:42px;top:88px;background:var(--orange)"><svg width="7" height="9" viewBox="0 0 7 9"><rect x=".5" y=".5" width="6" height="8" fill="none" stroke="#fff" stroke-width=".8"/><path d="M2 3h3M2 5h3M2 7h2" stroke="#fff" stroke-width=".6"/></svg></div>
  <div class="row-text" style="top:88px"><div class="row-head">TEXT GOES HERE</div><p class="tiny">Lorem ipsum dolor sit amet, tempor incididunt ut labore et dolore magna aliqua.</p></div>
  <div class="icon-dot" style="left:42px;top:126px;background:var(--amber)"><svg width="7" height="9" viewBox="0 0 7 9"><path d="M1.5 4V2.8a2 2 0 0 1 4 0V4" fill="none" stroke="#fff" stroke-width=".8"/><rect x=".5" y="4" width="6" height="4.5" fill="#fff"/></svg></div>
  <div class="row-text" style="top:126px"><div class="row-head">TEXT GOES HERE</div><p class="tiny">Lorem ipsum dolor sit amet, tempor incididunt ut labore et dolore magna aliqua.</p></div>
  <footer class="foot"><span class="foot-url">WWW.TERVALO.COM</span></footer><div class="page">1</div>
</section>

<!-- Row 2 -->
<section class="slide" style="left:51px;top:213px">
  <h2 class="s-title">TITLE GOES HERE</h2><div class="brand">Tervalo</div>
  <div class="num" style="left:101px;top:57px;background:var(--navy)">01</div>
  <div class="num" style="left:123px;top:57px;background:var(--orange)">02</div>
  <div class="num" style="left:101px;top:82px;background:var(--amber)">03</div>
  <div class="num" style="left:123px;top:82px;background:var(--navy)">04</div>
  <div class="num" style="left:101px;top:108px;background:var(--orange)">05</div>
  <div class="num" style="left:123px;top:108px;background:var(--amber)">06</div>
  <div class="grid-text right" style="left:18px;top:55px"><h4>Title here</h4><p>Lorem ipsum dolor sit amet consectetur adipisicing elit</p></div>
  <div class="grid-text right" style="left:18px;top:80px"><h4>Title here</h4><p>Lorem ipsum dolor sit amet consectetur adipisicing elit</p></div>
  <div class="grid-text right" style="left:18px;top:106px"><h4>Title here</h4><p>Lorem ipsum dolor sit amet consectetur adipisicing elit</p></div>
  <div class="grid-text" style="left:146px;top:55px"><h4>Title here</h4><p>Lorem ipsum dolor sit amet consectetur adipisicing elit</p></div>
  <div class="grid-text" style="left:146px;top:80px"><h4>Title here</h4><p>Lorem ipsum dolor sit amet consectetur adipisicing elit</p></div>
  <div class="grid-text" style="left:146px;top:106px"><h4>Title here</h4><p>Lorem ipsum dolor sit amet consectetur adipisicing elit</p></div>
  <footer class="foot"><span class="foot-url">WWW.TERVALO.COM</span></footer><div class="page">1</div>
</section>

<section class="slide" style="left:308px;top:213px">
  <h2 class="s-title">TITLE GOES HERE</h2><div class="brand">Tervalo</div>
  <div class="abs bold" style="left:21px;top:43px;font:700 5px/1 'Open Sans',sans-serif">SUBHEADING GOES HERE</div>
  <p class="abs small" style="left:21px;top:56px;width:200px">Lorem ipsum dolor sit amet, consectetur adipisicing elit, sed do eiusmod tempor incididunt ut labore et dolore magna aliqua. Ut enim ad minim veniam, quis nostrud exercitation ullamco laboris nisi ut aliquip ex ea commodo consequat. Duis aute irure dolor in reprehenderit in voluptate velit esse cillum dolore eu fugiat nulla pariatur.</p>
  <p class="abs small" style="left:21px;top:96px;width:200px">Lorem ipsum dolor sit amet, consectetur adipisicing elit, sed do eiusmod tempor incididunt ut labore et dolore magna aliqua. Ut enim ad minim veniam, quis nostrud exercitation ullamco laboris nisi ut aliquip ex ea commodo consequat. Duis aute irure dolor in reprehenderit in voluptate velit esse cillum dolore eu fugiat nulla pariatur.</p>
  <footer class="foot"><span class="foot-url">WWW.TERVALO.COM</span></footer><div class="page">2</div>
</section>

<section class="slide" style="left:566px;top:213px">
  <h2 class="s-title">TITLE GOES HERE</h2><div class="brand">Tervalo</div>
  <div class="abs" style="left:99px;top:53px;width:43px;height:43px;border-radius:50%;background:var(--orange);color:var(--navy);font:700 34px/60px Georgia,serif;text-align:center">&ldquo;</div>
  <div class="abs" style="left:22px;top:105px;width:197px;height:.6px;background:#d6d8dc"></div>
  <p class="abs small" style="left:34px;top:110px;width:175px">Lorem ipsum dolor sit amet, consectetur adipisicing elit, sed do eiusmod tempor incididunt ut labore et dolore magna aliqua. Ut enim ad minim veniam, quis nostrud commodo consequat.</p>
  <footer class="foot"><span class="foot-url">WWW.TERVALO.COM</span></footer><div class="page">3</div>
</section>

<!-- Row 3 -->
<section class="slide" style="left:51px;top:411px">
  <h2 class="s-title">TITLE GOES HERE</h2>
  <div class="abs bold" style="left:14px;top:44px;font:700 6.5px/1.15 'Poppins',sans-serif">OUR<br>PHILOSOPHY</div>
  <p class="abs small" style="left:14px;top:60px;width:74px;text-align:justify">Lorem ipsum dolor sit amet, consectetur adipisicing elit, sed do eiusmod tempor incididunt ut labore et dolore magna aliqua. Ut enim ad minim veniam, commodo consequat. Duis aute irure dolor in reprehenderit in voluptate velit esse cillum dolore eu fugiat nulla pariatur.</p>
  <div class="abs" style="left:112px;top:38px;font:600 18px/1 'Poppins',sans-serif;color:var(--navy)">Tervalo</div>
  <div class="abs" style="left:97px;top:82px"><div class="pill-head">MISSION</div><p class="tiny" style="width:62px">Lorem ipsum dolor sit amet, consectetur adipisicing elit, sed do eiusmod tempor incididunt.</p></div>
  <div class="abs" style="left:170px;top:82px"><div class="pill-head" style="width:58px">VALUES</div><p class="tiny" style="width:58px">Lorem ipsum dolor sit amet, consectetur adipisicing elit, sed do eiusmod tempor incididunt.</p></div>
  <div class="abs" style="left:97px;top:116px"><div class="pill-head">VISION</div><p class="tiny" style="width:62px">Lorem ipsum dolor sit amet, consectetur adipisicing elit, sed do eiusmod tempor incididunt.</p></div>
  <div class="abs" style="left:170px;top:116px"><div class="pill-head" style="width:58px">GOALS</div><p class="tiny" style="width:58px"><span style="color:var(--orange)">•</span> Lorem ipsum dolor sit amet<br><span style="color:var(--orange)">•</span> Lorem ipsum dolor sit amet<br><span style="color:var(--orange)">•</span> Lorem ipsum dolor sit amet</p></div>
  <footer class="foot"><span class="foot-url">WWW.TERVALO.COM</span></footer><div class="page">1</div>
</section>

<section class="slide" style="left:308px;top:411px">
  <h2 class="s-title">TITLE GOES HERE</h2><div class="brand">Tervalo</div>
  <p class="abs small" style="left:19px;top:44px;width:200px;font-size:4px"><b style="color:var(--navy)">Lorem ipsum dolor sit amet, consectetur adipisicing elit, sed do eiusmod tempor incididunt ut labore et dolore magna aliqua. Ut enim ad minim veniam,</b> quis nostrud exercitation ullamco laboris nisi ut aliquip ex ea commodo consequat. Duis aute irure dolor in reprehenderit in voluptate velit esse cillum dolore eu fugiat nulla pariatur.</p>
  <ul class="abs checks" style="left:59px;top:83px">
    <li><svg width="4" height="4"><circle cx="2" cy="2" r="1.6" fill="none" stroke="#1b2535" stroke-width=".5"/><path d="M1.2 2l.6.6 1-1.1" stroke="#1b2535" stroke-width=".5" fill="none"/></svg>Lorem ipsum dolor sit amet</li>
    <li style="color:var(--orange)"><svg width="4" height="4"><circle cx="2" cy="2" r="1.6" fill="none" stroke="#f15a24" stroke-width=".5"/><path d="M1.2 2l.6.6 1-1.1" stroke="#f15a24" stroke-width=".5" fill="none"/></svg>Ut enim ad minim veniam</li>
    <li><svg width="4" height="4"><circle cx="2" cy="2" r="1.6" fill="none" stroke="#1b2535" stroke-width=".5"/><path d="M1.2 2l.6.6 1-1.1" stroke="#1b2535" stroke-width=".5" fill="none"/></svg>Incididunt ut labore et dolore magna</li>
    <li><svg width="4" height="4"><circle cx="2" cy="2" r="1.6" fill="none" stroke="#1b2535" stroke-width=".5"/><path d="M1.2 2l.6.6 1-1.1" stroke="#1b2535" stroke-width=".5" fill="none"/></svg>Esse cillum dolore eu fugiat nulla pariatur</li>
    <li style="color:var(--orange)"><svg width="4" height="4"><circle cx="2" cy="2" r="1.6" fill="none" stroke="#f15a24" stroke-width=".5"/><path d="M1.2 2l.6.6 1-1.1" stroke="#f15a24" stroke-width=".5" fill="none"/></svg>Dolor in reprehenderit in voluptate</li>
    <li style="color:var(--orange)"><svg width="4" height="4"><circle cx="2" cy="2" r="1.6" fill="none" stroke="#f15a24" stroke-width=".5"/><path d="M1.2 2l.6.6 1-1.1" stroke="#f15a24" stroke-width=".5" fill="none"/></svg>Nisi ut aliquip ex ea</li>
  </ul>
  <footer class="foot"><span class="foot-url">WWW.TERVALO.COM</span></footer><div class="page">1</div>
</section>

<section class="slide" style="left:566px;top:411px">
  <h2 class="s-title">TITLE GOES HERE</h2><div class="brand">Tervalo</div>
  <div class="abs" style="left:20px;top:44px;width:76px;height:46px;background:var(--navy);padding:4px"><p class="tiny" style="color:#fff;font-size:3px;text-align:justify">Lorem ipsum dolor sit amet, consectetur adipiscing elit, sed do eiusmod tempor incididunt ut labore et dolore magna aliqua. Ut enim ad minim veniam, quis nostrud exercitation. Duis aute irure dolor in reprehenderit in voluptate velit esse cillum.</p></div>
  <div class="abs" style="left:101px;top:44px;width:120px;height:46px;background:var(--amber);padding:4px"><p class="tiny" style="color:#fff;font-size:3px">Sed ut perspiciatis unde omnis iste natus error sit voluptatem accusantium doloremque laudantium, totam rem aperiam, eaque ipsa quae ab illo inventore veritatis et quasi architecto beatae vitae dicta sunt explicabo. Nemo enim ipsam voluptatem quia voluptas sit aspernatur aut odit aut fugit.</p></div>
  <div class="photo" role="img" aria-label="Photo of devices on a desk" style="left:20px;top:99px;width:49px;height:50px;background:linear-gradient(160deg,#e3e5e8,#8e949d)"></div>
  <div class="photo" role="img" aria-label="Photo of a team meeting in an office" style="left:74px;top:99px;width:75px;height:50px;background:linear-gradient(160deg,#dcdfe3,#9a9488)"></div>
  <div class="photo" role="img" aria-label="Photo of data charts on a monitor" style="left:154px;top:99px;width:67px;height:50px;background:linear-gradient(160deg,#3a4458,#9fb2c9)"></div>
  <footer class="foot"><span class="foot-url">WWW.TERVALO.COM</span></footer><div class="page">1</div>
</section>

<!-- Row 4 -->
<section class="slide" style="left:51px;top:608px">
  <h2 class="s-title">TITLE GOES HERE</h2><div class="brand">Tervalo</div>
  <svg class="abs" style="left:0;top:0" width="241" height="180" viewBox="0 0 241 180">
    <g fill="none" stroke-width="6">
      <path d="M15 90a21 21 0 0 1 42 0" stroke="#1b2535"/>
      <path d="M57 90a21 21 0 0 0 42 0" stroke="#f15a24"/>
      <path d="M99 90a21 21 0 0 1 42 0" stroke="#f7941d"/>
      <path d="M141 90a21 21 0 0 0 42 0" stroke="#1b2535"/>
      <path d="M183 90a21 21 0 0 1 42 0" stroke="#f15a24"/>
    </g>
    <g fill="#8b9099"><circle cx="36" cy="90" r="8"/><circle cx="78" cy="90" r="8"/><circle cx="120" cy="90" r="8"/><circle cx="162" cy="90" r="8"/><circle cx="204" cy="90" r="8"/></g>
    <g fill="none" stroke="#fff" stroke-width=".8">
      <circle cx="36" cy="89" r="1.5"/><path d="M33 93a3 3 0 0 1 6 0"/>
      <rect x="75" y="87" width="6" height="4" rx="1"/>
      <circle cx="120" cy="90" r="3"/><path d="M117 90h6M120 87v6"/>
      <circle cx="162" cy="90" r="3"/><circle cx="162" cy="90" r="1" fill="#fff"/>
      <rect x="201" y="87" width="6" height="6"/><path d="M204 92v-3M202.8 90.2l1.2-1.2 1.2 1.2"/>
    </g>
  </svg>
  <div class="abs center" style="left:53px;top:46px;width:50px"><div class="row-head">PROCESS 2</div><p class="tiny" style="font-size:3px">Lorem ipsum dolor sit amet, tempor incididunt ut labore et dolore magna aliqua.</p></div>
  <div class="abs center" style="left:137px;top:46px;width:50px"><div class="row-head">PROCESS 4</div><p class="tiny" style="font-size:3px">Lorem ipsum dolor sit amet, tempor incididunt ut labore et dolore magna aliqua.</p></div>
  <div class="abs center" style="left:11px;top:116px;width:50px"><div class="row-head">PROCESS 1</div><p class="tiny" style="font-size:3px">Lorem ipsum dolor sit amet, tempor incididunt ut labore et dolore magna aliqua.</p></div>
  <div class="abs center" style="left:95px;top:116px;width:50px"><div class="row-head">PROCESS 3</div><p class="tiny" style="font-size:3px">Lorem ipsum dolor sit amet, tempor incididunt ut labore et dolore magna aliqua.</p></div>
  <div class="abs center" style="left:179px;top:116px;width:50px"><div class="row-head">PROCESS 5</div><p class="tiny" style="font-size:3px">Lorem ipsum dolor sit amet, tempor incididunt ut labore et dolore magna aliqua.</p></div>
  <footer class="foot"><span class="foot-url">WWW.TERVALO.COM</span></footer><div class="page">1</div>
</section>

<section class="slide" style="left:308px;top:608px">
  <div class="photo" role="img" aria-label="Photo of a laptop showing a media gallery" style="left:0;top:0;width:241px;height:84px;background:linear-gradient(120deg,#f1f2f4 0%,#c7ccd4 45%,#6e7888 100%)"></div>
  <h2 class="s-title">TITLE GOES HERE</h2><div class="brand">Tervalo</div>
  <div class="num" style="left:42px;top:90px;width:22px;height:22px;border-radius:50%;line-height:22px;background:var(--navy)">1</div>
  <div class="num" style="left:110px;top:90px;width:22px;height:22px;border-radius:50%;line-height:22px;background:var(--orange)">2</div>
  <div class="num" style="left:176px;top:90px;width:22px;height:22px;border-radius:50%;line-height:22px;background:var(--amber)">3</div>
  <div class="abs center" style="left:28px;top:119px;width:50px"><div class="row-head">TEXT GOES HERE</div><p class="tiny" style="font-size:3px">Lorem ipsum dolor sit amet, tempor incididunt ut labore et dolore magna aliqua.</p></div>
  <div class="abs center" style="left:96px;top:119px;width:50px"><div class="row-head">TEXT GOES HERE</div><p class="tiny" style="font-size:3px">Lorem ipsum dolor sit amet, tempor incididunt ut labore et dolore magna aliqua.</p></div>
  <div class="abs center" style="left:162px;top:119px;width:50px"><div class="row-head">TEXT GOES HERE</div><p class="tiny" style="font-size:3px">Lorem ipsum dolor sit amet, tempor incididunt ut labore et dolore magna aliqua.</p></div>
  <footer class="foot"><span class="foot-url">WWW.TERVALO.COM</span></footer><div class="page">1</div>
</section>

<section class="slide" style="left:566px;top:608px">
  <h2 class="s-title">TITLE GOES HERE</h2><div class="brand">Tervalo</div>
  <table class="table">
    <tr><th style="background:var(--navy);width:52px">Subheading one</th><th style="background:var(--orange)">Subheading two</th><th style="background:var(--amber)">Subheading three</th><th style="background:#98a3b3">Subheading four</th></tr>
    <tr><td>Lorem ipsum du sit</td><td>Dolor</td><td>Dolor</td><td>Dolor</td></tr>
    <tr><td>Lorem ipsum du sit</td><td>Dolor</td><td>Dolor</td><td>Dolor</td></tr>
    <tr><td>Lorem ipsum du sit</td><td>Dolor</td><td>Dolor</td><td>Dolor</td></tr>
    <tr><td>Lorem ipsum du sit</td><td>Dolor</td><td>Dolor</td><td>Dolor</td></tr>
    <tr><td>Lorem ipsum du sit</td><td>Dolor</td><td>Dolor</td><td>Dolor</td></tr>
  </table>
  <footer class="foot"><span class="foot-url">WWW.TERVALO.COM</span></footer><div class="page">1</div>
</section>

<!-- Row 5 -->
<section class="slide" style="left:51px;top:806px">
  <h2 class="s-title">TITLE GOES HERE</h2><div class="brand">Tervalo</div>
  <svg class="abs" style="left:0;top:0" width="241" height="180" viewBox="0 0 241 180">
    <g fill="none" stroke-width="11">
      <circle cx="121" cy="86" r="22" stroke="#1b2535" stroke-dasharray="32 106" transform="rotate(182 121 86)"/>
      <circle cx="121" cy="86" r="22" stroke="#f15a24" stroke-dasharray="32 106" transform="rotate(272 121 86)"/>
      <circle cx="121" cy="86" r="22" stroke="#f7941d" stroke-dasharray="32 106" transform="rotate(2 121 86)"/>
      <circle cx="121" cy="86" r="22" stroke="#a9adb4" stroke-dasharray="32 106" transform="rotate(92 121 86)"/>
    </g>
    <g stroke="#8b9099" stroke-width=".5" fill="#8b9099">
      <path d="M80 56h14l4 6" fill="none"/><circle cx="98" cy="62" r="1"/>
      <path d="M162 56h-14l-4 6" fill="none"/><circle cx="144" cy="62" r="1"/>
      <path d="M80 120h14l4-6" fill="none"/><circle cx="98" cy="114" r="1"/>
      <path d="M162 120h-14l-4-6" fill="none"/><circle cx="144" cy="114" r="1"/>
    </g>
  </svg>
  <div class="abs" style="left:17px;top:48px;width:70px"><h4 style="font:700 5.5px/1.3 'Open Sans',sans-serif;color:var(--navy)">Text Title</h4><p class="small" style="font-size:3.8px">Lorem ipsum dolor sit amet, consectetur adipisicing elit, sed do eiusmod tempor incididunt ut labore et dolore</p></div>
  <div class="abs" style="left:165px;top:48px;width:70px"><h4 style="font:700 5.5px/1.3 'Open Sans',sans-serif;color:var(--orange)">Text Title</h4><p class="small" style="font-size:3.8px">Lorem ipsum dolor sit amet, consectetur adipisicing elit, sed do eiusmod tempor incididunt ut labore et dolore</p></div>
  <div class="abs" style="left:17px;top:118px;width:70px"><h4 style="font:700 5.5px/1.3 'Open Sans',sans-serif;color:#a9adb4">Text Title</h4><p class="small" style="font-size:3.8px">Lorem ipsum dolor sit amet, consectetur adipisicing elit, sed do eiusmod tempor incididunt ut labore et dolore</p></div>
  <div class="abs" style="left:165px;top:118px;width:70px"><h4 style="font:700 5.5px/1.3 'Open Sans',sans-serif;color:var(--amber)">Text Title</h4><p class="small" style="font-size:3.8px">Lorem ipsum dolor sit amet, consectetur adipisicing elit, sed do eiusmod tempor incididunt ut labore et dolore</p></div>
  <footer class="foot"><span class="foot-url">WWW.TERVALO.COM</span></footer><div class="page">1</div>
</section>

<section class="slide" style="left:308px;top:806px">
  <h2 class="s-title">TITLE GOES HERE</h2><div class="brand">Tervalo</div>
  <svg class="abs" style="left:0;top:0" width="241" height="180" viewBox="0 0 241 180" font-family="Open Sans, sans-serif">
    <g font-size="3.6" fill="#3c4350" text-anchor="end">
      <text x="30" y="63">250</text><text x="30" y="76">200</text><text x="30" y="89">150</text><text x="30" y="102">100</text><text x="30" y="115">50</text>
    </g>
    <path d="M34 128h108" stroke="#1b2535" stroke-width=".6"/>
    <g>
      <rect x="40" y="95" width="6" height="33" fill="#1b2535"/><rect x="46" y="78" width="6" height="50" fill="#f15a24"/><rect x="52" y="110" width="6" height="18" fill="#f7941d"/>
      <rect x="67" y="104" width="6" height="24" fill="#1b2535"/><rect x="73" y="85" width="6" height="43" fill="#f15a24"/><rect x="79" y="113" width="6" height="15" fill="#f7941d"/>
      <rect x="94" y="98" width="6" height="30" fill="#1b2535"/><rect x="100" y="90" width="6" height="38" fill="#f15a24"/><rect x="106" y="108" width="6" height="20" fill="#f7941d"/>
      <rect x="121" y="108" width="6" height="20" fill="#1b2535"/><rect x="127" y="76" width="6" height="52" fill="#f15a24"/><rect x="133" y="64" width="6" height="64" fill="#f7941d"/>
    </g>
    <g font-size="3.6" font-weight="700" fill="#1b2535" text-anchor="middle">
      <text x="49" y="134">TEXT</text><text x="76" y="134">TEXT</text><text x="103" y="134">TEXT</text><text x="130" y="134">TEXT</text>
    </g>
    <rect x="157" y="56" width="3" height="3" fill="#1b2535"/><rect x="157" y="79" width="3" height="3" fill="#f15a24"/><rect x="157" y="102" width="3" height="3" fill="#f7941d"/>
  </svg>
  <div class="abs" style="left:163px;top:55px;width:50px"><div class="row-head">Title Text</div><p class="tiny" style="font-size:3px">Lorem ipsum dolor sit amet, consectetur adipisicing, sed do eiusmod tempor</p></div>
  <div class="abs" style="left:163px;top:78px;width:50px"><div class="row-head" style="color:var(--orange)">Title Text</div><p class="tiny" style="font-size:3px">Lorem ipsum dolor sit amet, consectetur adipisicing, sed do eiusmod tempor</p></div>
  <div class="abs" style="left:163px;top:101px;width:50px"><div class="row-head" style="color:var(--amber)">Title Text</div><p class="tiny" style="font-size:3px">Lorem ipsum dolor sit amet, consectetur adipisicing, sed do eiusmod tempor</p></div>
  <footer class="foot"><span class="foot-url">WWW.TERVALO.COM</span></footer><div class="page">1</div>
</section>

<section class="slide" style="left:566px;top:806px">
  <h2 class="s-title">TITLE GOES HERE</h2><div class="brand">Tervalo</div>
  <svg class="abs" style="left:0;top:0" width="241" height="180" viewBox="0 0 241 180" font-family="Poppins, sans-serif">
    <g fill="none" stroke-width="3.5">
      <circle cx="40" cy="80" r="17" stroke="#e3e5e8"/><circle cx="40" cy="80" r="17" stroke="#f15a24" stroke-dasharray="26.7 80.1" transform="rotate(-90 40 80)"/>
      <circle cx="93" cy="80" r="17" stroke="#e3e5e8"/><circle cx="93" cy="80" r="17" stroke="#f15a24" stroke-dasharray="53.4 53.4" transform="rotate(-90 93 80)"/>
      <circle cx="147" cy="80" r="17" stroke="#e3e5e8"/><circle cx="147" cy="80" r="17" stroke="#f15a24" stroke-dasharray="74.8 32" transform="rotate(-90 147 80)"/>
      <circle cx="201" cy="80" r="17" stroke="#f15a24"/>
    </g>
    <g font-size="7.5" font-weight="600" fill="#1b2535" text-anchor="middle">
      <text x="40" y="83">25%</text><text x="93" y="83">50%</text><text x="147" y="83">70%</text><text x="201" y="83">100%</text>
    </g>
  </svg>
  <p class="pct small bold" style="left:15px;top:103px;font-weight:600">Lorem ipsum dolor sit amet consectetur</p>
  <p class="pct small bold" style="left:68px;top:103px;font-weight:600">Lorem ipsum dolor sit amet consectetur</p>
  <p class="pct small bold" style="left:122px;top:103px;font-weight:600">Lorem ipsum dolor sit amet consectetur</p>
  <p class="pct small bold" style="left:176px;top:103px;font-weight:600">Lorem ipsum dolor sit amet consectetur</p>
  <footer class="foot"><span class="foot-url">WWW.TERVALO.COM</span></footer><div class="page">1</div>
</section>

<!-- Row 6 -->
<section class="slide" style="left:51px;top:1004px">
  <h2 class="s-title">TITLE GOES HERE</h2><div class="brand">Tervalo</div>
  <div class="person" style="left:6px;top:41px"><div class="avatar" role="img" aria-label="Team member portrait"></div><h5>Jonathan Doe</h5><p class="tiny" style="font-size:3.2px">Lorem ipsum dolor sit amet, consectetur adipisicing elit, sed do eiusmod tempor incididunt ut labore et dolore magna aliqua.</p><p class="tiny" style="font-size:3.2px;margin-top:3px">Ut enim ad minim veniam, quis nostrud exercitation ullamco laboris nisi ut aliquip ex ea commodo consequat.</p></div>
  <div class="person" style="left:82px;top:41px"><div class="avatar" role="img" aria-label="Team member portrait"></div><h5>Jonathan Doe</h5><p class="tiny" style="font-size:3.2px">Lorem ipsum dolor sit amet, consectetur adipisicing elit, sed do eiusmod tempor incididunt ut labore et dolore magna aliqua.</p><p class="tiny" style="font-size:3.2px;margin-top:3px">Ut enim ad minim veniam, quis nostrud exercitation ullamco laboris nisi ut aliquip ex ea commodo consequat.</p></div>
  <div class="person" style="left:160px;top:41px"><div class="avatar" role="img" aria-label="Team member portrait"></div><h5>Jonathan Doe</h5><p class="tiny" style="font-size:3.2px">Lorem ipsum dolor sit amet, consectetur adipisicing elit, sed do eiusmod tempor incididunt ut labore et dolore magna aliqua.</p><p class="tiny" style="font-size:3.2px;margin-top:3px">Ut enim ad minim veniam, quis nostrud exercitation ullamco laboris nisi ut aliquip ex ea commodo consequat.</p></div>
  <footer class="foot"><span class="foot-url">WWW.TERVALO.COM</span></footer><div class="page">1</div>
</section>

<section class="slide" style="left:308px;top:1004px">
  <h2 class="s-title">TITLE GOES HERE</h2><div class="brand">Tervalo</div>
  <p class="abs small" style="left:19px;top:43px;width:203px">Lorem ipsum dolor sit amet, consectetur adipisicing elit, sed do eiusmod tempor incididunt ut labore et dolore magna aliqua. Ut enim ad minim veniam, quis nostrud exercitation ullamco laboris nisi ut aliquip ex ea commodo consequat. Duis aute irure dolor in reprehenderit in voluptate velit esse cillum dolore eu fugiat nulla pariatur. Excepteur sint occaecat cupidatat non proident, sunt in culpa qui officia deserunt mollit anim id est laborum. Sed ut perspiciatis unde omnis iste natus error sit voluptatem accusantium doloremque laudantium, totam rem aperiam, eaque ipsa quae ab illo inventore veritatis et quasi.</p>
  <div class="abs" style="left:15px;top:108px;width:211px;height:25px;background:var(--orange);padding:3px 5px"><p class="small" style="color:#fff;font-size:4px">Lorem ipsum dolor sit amet, consectetur adipisicing elit, sed do eiusmod tempor incididunt ut labore et dolore magna aliqua. Ut enim ad minim veniam, quis nostrud exercitation ullamco laboris nisi ut aliquip ex ea commodo consequat.</p></div>
  <footer class="foot"><span class="foot-url">WWW.TERVALO.COM</span></footer><div class="page">1</div>
</section>

<section class="slide" style="left:566px;top:1004px">
  <div class="abs" style="left:22px;top:30px;font:600 17px/1 'Poppins',sans-serif;color:var(--navy)">Tervalo</div>
  <div class="abs" style="left:76px;top:87px;font:700 11px/1 'Poppins',sans-serif;color:var(--navy);letter-spacing:.8px">THANK YOU</div>
  <div class="abs" style="left:22px;top:127px;font:400 7px/1 'Open Sans',sans-serif;color:var(--navy);padding-bottom:2px;border-bottom:.6px solid var(--navy)">Contact Us</div>
  <ul class="abs contact" style="left:31px;top:141px">
    <li><i></i>(123) 456-7890</li>
    <li><i></i>mail@website.com</li>
    <li><i></i>www.website.com</li>
    <li><i></i>Street No., Location</li>
  </ul>
</section>

</body>
</html>
```